Small scale cold brew coffee producer needs a label for its products

We are a cold brew coffee producer and am now going the next step and getting our products onto the retail market.
Cold brewed coffee is coffee that which is brewed over a long period of time so its coffee which is brewed opposed to boiled this allows for a smoother taste and removes the acidic taste note often experienced in hot normal coffee. We currently offer three varieties from this core product. The first being a ready to drink neat version, the second being coffee and milk and the final a coffee and coconut milk.
In terms of design of the label i am looking for an artisan style to maintain the craft nature of the product. yet possible the use of abstract art to increase the appeal of it on the shelf.
in terms of a message i am looking to portray one of the quality of our product such as no additives and the use of specialist grade coffee that is in season.
As a colour scheme i am pretty flexible except to that of bright blue and white as it has too much of a similarity to heath products.
The images below are possible ideas and my current logo

Target Market(s)

As i am using spiciest grade coffee this will create a high price point. Current consumption statistics suggest that the major consumption group is the 20 - 40 year olds working professional. Yet its a popular product in arty urban centers such as brighton and bristol

Industry/Entity Type

Retail

Font styles to use
Serif
Script

Requirements
Must have
• The use of graphics and images to better poetry the image for the product, yet i am still looking for a classical appearance so old school outer labels, but the most important feature will be to maintain the arazan appearance for the product
Nice to have
• If i could have a sharp contrast between the difference and the product so a sharp difference. Gentle colours which are not too sharp and bold but more mellow. Possible use of abstract art in the text to improve the overall apperance
Should not have
• modern sharp images as i want an old school type image, I don't want sharp whites, blues and reds as they are too closely related to the heath care

```html
<!DOCTYPE html>
<html lang="en">
<head>
<meta charset="utf-8">
<title>Harlow's Cold Brewed Coffee – Milk Label</title>
<link rel="stylesheet" href="https://fonts.googleapis.com/css2?family=Lato:wght@400;700;900&family=Anton&display=swap">
<style>
  :root {
    --backdrop-light: #f7f7f7;
    --backdrop-dark: #e2e2e2;
    --cream: #fdf6e3;
    --brand-red: #e02b2b;
    --ink: #111111;
    --brown: #3a2a22;
    --white: #ffffff;
    --bean-dark: #161010;
  }
  * { box-sizing: border-box; margin: 0; padding: 0; }
  html, body { width: 1200px; height: 1000px; overflow: hidden; }
  body {
    background: radial-gradient(ellipse at center, var(--backdrop-light) 0%, var(--backdrop-dark) 100%);
    font-family: "Lato", sans-serif;
    color: var(--ink);
    position: relative;
  }
  .label {
    position: absolute;
    left: 121px; top: 267px;
    width: 956px; height: 466px;
    background: var(--cream);
    box-shadow: 0 1px 4px rgba(0,0,0,0.25);
    overflow: hidden;
  }
  .info-left { position: absolute; left: 29px; top: 21px; width: 270px; }
  .info-heading { color: var(--brand-red); font-weight: 700; font-size: 14px; line-height: 17px; }
  .info-text { font-size: 13px; line-height: 17px; }
  .info-block + .info-block { margin-top: 17px; }

  .warning {
    position: absolute; left: 27px; top: 162px;
    width: 264px; height: 92px;
    background: var(--brand-red);
    color: var(--white);
    text-align: center;
    font-weight: 700; font-size: 16.5px; line-height: 18.5px;
    padding-top: 7px;
  }
  .warning-title { font-size: 18px; }
  .brew-date { position: absolute; left: 29px; top: 267px; font-weight: 700; font-size: 14px; }
  .brew-date-field { position: absolute; left: 27px; top: 285px; width: 264px; height: 33px; background: var(--white); }
  .recycle { position: absolute; left: 27px; top: 326px; }

  .brand-mark {
    position: absolute; left: 362px; top: 40px; width: 230px; height: 130px;
    display: flex; align-items: center; justify-content: center; gap: 10px;
  }
  .brand-dot { width: 14px; height: 14px; border-radius: 50%; background: var(--brand-red); flex: none; }
  .brand-name { color: var(--brown); font-weight: 900; font-size: 22px; line-height: 25px; text-align: center; }

  .claims { position: absolute; left: 324px; top: 212px; width: 309px; font-family: "Anton", sans-serif; color: var(--ink); }
  .rule { height: 3px; background: var(--ink); }
  .claims-row { display: flex; height: 100px; padding-top: 3px; }
  .claims-left { width: 172px; line-height: 0.92; border-right: 2px solid var(--ink); }
  .claims-left span { display: block; }
  .cl-1 { font-size: 29px; letter-spacing: -0.3px; }
  .cl-2 { font-size: 30px; letter-spacing: -0.3px; }
  .cl-3 { font-size: 44px; letter-spacing: -0.5px; }
  .claims-right { flex: 1; padding-left: 6px; line-height: 0.93; }
  .cr-1 { display: block; font-size: 50px; }
  .cr-2 { display: block; font-size: 52px; }
  .claims-bottom { font-size: 44px; line-height: 48px; text-align: center; letter-spacing: 0.3px; }

  .info-right { position: absolute; left: 670px; top: 21px; width: 270px; }
  .benefits { list-style: none; margin-top: 18px; }
  .benefits li { display: flex; gap: 10px; font-size: 13px; line-height: 17px; margin-bottom: 17px; }
  .benefit-bullet { flex: none; width: 12px; height: 15px; border-radius: 50%; background: var(--brand-red); margin-top: 1px; }

  .variant-band {
    position: absolute; left: 0; top: 377px; width: 956px; height: 89px;
    background: var(--brand-red); text-align: center; color: var(--white);
  }
  .variant-name { padding-top: 20px; font-weight: 700; font-size: 21px; letter-spacing: 5px; }
  .variant-volume { font-size: 12px; letter-spacing: 4px; margin-top: 8px; }
  .bean-pile {
    position: absolute; left: 0; bottom: 0; width: 956px; height: 34px;
    background: linear-gradient(to bottom, #2a1a16, var(--bean-dark));
    clip-path: polygon(0 40%, 6% 10%, 13% 30%, 21% 15%, 28% 45%, 34% 60%, 40% 70%, 60% 70%, 66% 60%, 72% 40%, 79% 15%, 86% 30%, 93% 5%, 100% 30%, 100% 100%, 0 100%);
  }
</style>
</head>
<body>
  <div class="label">
    <div class="info-left">
      <div class="info-block">
        <p class="info-heading">Ingredients:</p>
        <p class="info-text">Filtered water, whole milk, specialist grade coffee and cane sugar.</p>
      </div>
      <div class="info-block">
        <p class="info-heading">Keep refrigerated once opened</p>
        <p class="info-text">Use within 20 days of opening.<br>Store in an upright position.</p>
      </div>
    </div>

    <div class="warning">
      <div class="warning-title">WARNING!</div>
      Contains caffeine, also not suitable for people with lactose intolerance.
    </div>

    <p class="brew-date">Brew date:</p>
    <div class="brew-date-field"></div>

    <svg class="recycle" width="44" height="44" viewBox="0 0 44 44" aria-label="Recyclable">
      <g fill="none" stroke="#e02b2b" stroke-width="5" stroke-linejoin="round">
        <path d="M16 12 L22 3 L28 12"/>
        <path d="M34 22 L40 34 L29 34"/>
        <path d="M15 34 L4 34 L10 23"/>
      </g>
      <g fill="#e02b2b">
        <path d="M28 6 L33 15 L24 15 Z"/>
        <path d="M25 30 L25 39 L17 34 Z"/>
        <path d="M5 18 L14 17 L10 26 Z"/>
      </g>
    </svg>

    <div class="brand-mark">
      <span class="brand-dot"></span>
      <p class="brand-name">Harlow's<br>Cold Brewed Coffee</p>
    </div>

    <div class="claims">
      <div class="rule"></div>
      <div class="claims-row">
        <div class="claims-left">
          <span class="cl-1">MADE WITH</span>
          <span class="cl-2">SPECIALIST</span>
          <span class="cl-3">COFFEE</span>
        </div>
        <div class="claims-right">
          <span class="cr-1">100%</span>
          <span class="cr-2">PURE</span>
        </div>
      </div>
      <div class="rule"></div>
      <div class="claims-bottom">NO ADDITIVES</div>
      <div class="rule"></div>
    </div>

    <div class="info-right">
      <p class="info-heading">Harlow's Cold Brewed Coffee</p>
      <p class="info-text">A super smooth premium cold brewed coffee, crafted for your enjoyment from 100% specialist grade coffee beans. Our coffee is brewed low and slow for over 16 hours to create a smooth coffee which can be heated or enjoyed over ice.</p>
      <ul class="benefits">
        <li><span class="benefit-bullet"></span>Less caffeine than traditional coffee.</li>
        <li><span class="benefit-bullet"></span>Naturally sweeter taste, less acidic.</li>
        <li><span class="benefit-bullet"></span>Smoother taste than hot brewed coffee.</li>
      </ul>
    </div>

    <div class="variant-band">
      <p class="variant-name">MILK</p>
      <p class="variant-volume">330ml</p>
      <div class="bean-pile" role="img" aria-label="Pile of roasted coffee beans along the bottom edge"></div>
    </div>
  </div>
</body>
</html>
```